Business Card Design

Hello,
I try and keep my business card fresh and current. So about every year i get a new one. This year I'd like something with a white background and black lettering.
Before you start - I do not want my phone number or any other description on the card other than my url and my email.

I'd like a double sided business card with
TobFarnsby.com on one side

and

Tob@TobFarnsby.com on the other side of the card

Thinking very minimalistic and modern.
I don't have a particular font i mind or how to capitalize my name or website. This card will lead people to my new website that is being designed to showcase my photography and music.

* Initial thought was the front side of the card having a grid-like pattern built out of dashes or periods, with my website sitting within the pattern and on the back side my email on a stark white background. But that might look completely lame - haha.

I'm looking forward to seeing what you come up with.

thank you,
- tob farnsby

Reason: Want to spend some more time with the designs and add a little $. thanks for all the designs - tob

Wanted to add a little $ and spend some more time with the designs.

big thanks to all who have submitted work 

- tob

Industry/Entity Type

Business

Contact Information for Business Card

www.tobfarnsby.com
tob@tobfarnsby.com

Colors
000000
ffffff

Requirements
Must have
• tobfarnsby.com
tob@tobfarnsby.com
Should not have
• phone number
any description of what i do, photography or music

```html
<!DOCTYPE html>
<html lang="en">
<head>
<meta charset="utf-8">
<title>Tob Farnsby — Business Card</title>
<link rel="stylesheet" href="https://fonts.googleapis.com/css2?family=Lato:wght@300;400;700&display=swap">
<style>
  :root {
    --ink: #000000;
    --paper: #ffffff;
    --stage: #e4e4e4;
    --grid-tone-light: #f4f4f4;
    --grid-tone-dark: #e9e9e9;
    --card-shadow: rgba(0, 0, 0, 0.18);
  }

  * { box-sizing: border-box; margin: 0; padding: 0; }

  html, body {
    width: 1200px;
    height: 926px;
    overflow: hidden;
    background: var(--stage);
    font-family: "Lato", Arial, sans-serif;
  }

  .stage {
    width: 1200px;
    height: 926px;
    display: flex;
    flex-direction: column;
    align-items: center;
    justify-content: center;
    gap: 40px;
  }

  .card {
    position: relative;
    width: 720px;
    height: 412px;
    background: var(--paper);
    box-shadow: 0 6px 22px var(--card-shadow);
    overflow: hidden;
  }

  /* Front side: dot grid field with the web address band */
  .card-front .grid-field {
    position: absolute;
    inset: 0;
    background: linear-gradient(135deg, var(--grid-tone-light), var(--grid-tone-dark));
  }

  .card-front .url-band {
    position: absolute;
    left: 46%;
    right: 0;
    top: 61%;
    height: 36px;
    background: var(--ink);
    display: flex;
    align-items: center;
    padding-left: 22px;
  }

  .card-front .url {
    color: var(--paper);
    font-size: 24px;
    font-weight: 400;
    letter-spacing: 1.5px;
    white-space: nowrap;
  }

  /* Back side: name and email on plain white */
  .card-back .identity {
    position: absolute;
    left: 37%;
    top: 38%;
    color: var(--ink);
  }

  .card-back .name {
    font-size: 34px;
    line-height: 1;
    letter-spacing: 0.5px;
    text-transform: uppercase;
    white-space: nowrap;
  }

  .card-back .name-first { font-weight: 300; }
  .card-back .name-last { font-weight: 700; }

  .card-back .email {
    margin-top: 12px;
    font-size: 20px;
    font-weight: 400;
    letter-spacing: 0.5px;
  }
</style>
</head>
<body>
  <main class="stage">
    <section class="card card-front" aria-label="Card front">
      <div class="grid-field" role="img" aria-label="Fine black dot grid pattern on white"></div>
      <div class="url-band">
        <span class="url">www.TobFarnsby.com</span>
      </div>
    </section>

    <section class="card card-back" aria-label="Card back">
      <div class="identity">
        <h1 class="name"><span class="name-first">Tob</span> <span class="name-last">Farnsby</span></h1>
        <p class="email">tob@tobfarnsby.com</p>
      </div>
    </section>
  </main>
</body>
</html>
```